Create branded design templates/backgrounds for social media based on UK property investing company

I'd like Instagram, Facebook and Linkedin backgrounds/templates to add text to, based on my logo design and business of UK holiday let investing. Ideally I'd have some base designs for me to approve, then engage with the winning designer further to create about 50 different templates. I looking for a mixture of templates with the logo and using logo colours, others of internal holiday let photos including logos and a few of my photo imposed on the front of them.
Updates

Slow in providing feedback

Target Market(s)

Middle aged adults

Industry/Entity Type

Holiday let properties

Requirements
Must have
• a distinct brand look that can be replicated

```html
<!DOCTYPE html>
<html lang="en">
<head>
<meta charset="UTF-8">
<title>Harbourstone Lets – Holiday Let Social Template</title>
<link href="https://fonts.googleapis.com/css2?family=Poppins:wght@400;500;700;800&display=swap" rel="stylesheet">
<style>
  :root {
    --bg-light: #f7fbfe;
    --bg-blue: #c4e0f2;
    --brand-blue: #0585d0;
    --brand-green: #58a80a;
    --brand-yellow: #f8d62e;
    --ink-dark: #23252b;
    --ink-grey: #5d6068;
    --icon-grey: #55575c;
    --panel-top: #eeeeee;
    --panel-mid: #b4b6ba;
    --panel-bottom: #44474d;
    --headline: #f4f4f4;
    --tagline: #eef6bf;
  }
  html, body {
    margin: 0;
    padding: 0;
    width: 1200px;
    height: 1200px;
    overflow: hidden;
    background: var(--bg-light);
  }
  .social-post {
    display: block;
    width: 1200px;
    height: 1200px;
    font-family: 'Poppins', sans-serif;
  }
  .brand-name { font-size: 27px; font-weight: 500; fill: var(--ink-grey); }
  .intro-line { font-size: 26px; font-weight: 700; fill: var(--ink-dark); }
  .headline { font-size: 64px; font-weight: 800; fill: var(--headline); letter-spacing: 0.5px; }
  .tagline { font-size: 34px; font-weight: 700; fill: var(--tagline); }
  .currency-mark { font-size: 82px; font-weight: 800; fill: var(--ink-grey); }
  .web-address { font-size: 22px; font-weight: 500; fill: var(--ink-dark); }
</style>
</head>
<body>
<svg class="social-post" viewBox="0 0 1080 1080" xmlns="http://www.w3.org/2000/svg">
  <defs>
    <linearGradient id="page-bg" x1="1" y1="0" x2="0" y2="1">
      <stop offset="0" stop-color="var(--bg-light)"/>
      <stop offset="1" stop-color="var(--bg-blue)"/>
    </linearGradient>
    <linearGradient id="panel-fade" x1="0.6" y1="0" x2="0.15" y2="1">
      <stop offset="0" stop-color="var(--panel-top)"/>
      <stop offset="0.55" stop-color="var(--panel-mid)"/>
      <stop offset="1" stop-color="var(--panel-bottom)"/>
    </linearGradient>
    <clipPath id="panel-clip">
      <path d="M50,125 Q50,50 125,50 L385,50 C520,120 620,500 650,962 L90,962 Q50,962 50,922 Z"/>
    </clipPath>
    <filter id="soft-shadow" x="-10%" y="-10%" width="130%" height="130%">
      <feDropShadow dx="0" dy="4" stdDeviation="8" flood-color="#000" flood-opacity="0.25"/>
    </filter>
  </defs>

  <!-- background -->
  <rect class="page-bg" width="1080" height="1080" fill="url(#page-bg)"/>

  <!-- decorative circles -->
  <circle class="accent-sun" cx="470" cy="185" r="95" fill="var(--brand-yellow)"/>
  <circle class="accent-green-corner" cx="1010" cy="990" r="165" fill="var(--brand-green)"/>

  <!-- content block for text -->
  <rect class="content-block" x="440" y="200" width="590" height="762" rx="22" fill="var(--brand-blue)"/>

  <circle class="accent-yellow-corner" cx="965" cy="1090" r="135" fill="var(--brand-yellow)"/>

  <!-- main curved panel -->
  <g class="feature-panel" filter="url(#soft-shadow)">
    <path d="M50,125 Q50,50 125,50 L385,50 C520,120 620,500 650,962 L90,962 Q50,962 50,922 Z" fill="url(#panel-fade)"/>
  </g>
  <g clip-path="url(#panel-clip)">
    <path class="panel-green-wave" d="M50,620 C250,640 360,800 395,962 L50,962 Z" fill="var(--brand-green)"/>
  </g>

  <!-- brand -->
  <g class="brand">
    <rect x="66" y="70" width="50" height="50" rx="6" fill="var(--brand-blue)"/>
    <text class="brand-name" x="130" y="106">Harbourstone Lets</text>
  </g>

  <!-- social buttons -->
  <g class="social-links" fill="var(--icon-grey)">
    <circle cx="900" cy="69" r="18"/>
    <circle cx="956" cy="69" r="18"/>
    <circle cx="1012" cy="69" r="18"/>
  </g>

  <!-- headline copy -->
  <text class="intro-line" x="100" y="277">Turn your holiday</text>
  <text class="headline" x="95" y="345">STYLISH</text>
  <text class="headline" x="95" y="412">SEAMLESS</text>
  <text class="headline" x="95" y="478">SUCCESSFUL</text>

  <!-- currency badge -->
  <g class="currency-badge">
    <circle cx="235" cy="693" r="66" fill="var(--brand-yellow)" filter="url(#soft-shadow)"/>
    <text class="currency-mark" x="237" y="722" text-anchor="middle">£</text>
  </g>

  <!-- tagline -->
  <text class="tagline" x="97" y="860">UK HOLIDAY</text>
  <text class="tagline" x="97" y="902">LET INVESTING</text>

  <!-- website -->
  <g class="web-link">
    <circle cx="70" cy="1008" r="20" fill="var(--icon-grey)"/>
    <g fill="none" stroke="#fff" stroke-width="1.8">
      <circle cx="70" cy="1008" r="11"/>
      <ellipse cx="70" cy="1008" rx="5" ry="11"/>
      <line x1="59" y1="1008" x2="81" y2="1008"/>
      <line x1="61" y1="1002" x2="79" y2="1002"/>
      <line x1="61" y1="1014" x2="79" y2="1014"/>
    </g>
    <text class="web-address" x="100" y="1016">www.yourwebsiteurl.com</text>
  </g>
</svg>
</body>
</html>
```